Login screen design for grocery app

Hi,

We are working on a grocery delivery app and need a design for its launch screen. This is the screen where the user clicks on either Login or Register. You can see our current login screen (and app name) in the attached image. You should use the same background color.

We are looking for designs that have to do with groceries (fruits/vegetables/diary products/chocolate etc).

Note: We do not want a login form on the launch screen, only a Login and Register button.

Let me know if you have any questions.

Regards.

Industry/Entity Type

Grocery Store

Colors
886aae
6b449b
e34298
ffffff
9bcb3c
f78f20
f04a50
33b8a4
34a6d7

Requirements
Must have
• The design must have to do with groceries.

```html
<!DOCTYPE html>
<html lang="en">
<head>
<meta charset="utf-8">
<title>basko — Welcome</title>
<link href="https://fonts.googleapis.com/css2?family=Open+Sans:wght@300;400&display=swap" rel="stylesheet">
<style>
  :root {
    --purple: #6b449b;
    --purple-soft: #8a6cb0;
    --lavender: #a696c4;
    --white: #ffffff;
    --orange: #f78f20;
    --blue: #34a6d7;
    --navy: #3a5b9c;
    --divider: #e8e6ec;
    --ink: #2e2a3a;
    --leaf: #6f9a4a;
    --tomato: #c8504e;
    --cream: #e6d9b8;
    --pasta: #e9c46a;
    --wood: #8a5a3c;
    --olive: #5d6b3a;
  }
  * { box-sizing: border-box; margin: 0; padding: 0; }
  html, body { width: 1200px; height: 2356px; overflow: hidden; }
  body {
    position: relative;
    font-family: "Open Sans", Arial, sans-serif;
    background: linear-gradient(180deg, var(--purple) 0%, var(--purple) 52%, var(--purple-soft) 66%, var(--lavender) 80%);
  }
  .brand {
    position: absolute; left: 0; right: 0; top: 300px;
    text-align: center; color: var(--white);
    font-weight: 300; font-size: 210px; line-height: 1; letter-spacing: 2px;
  }
  .btn-wide {
    position: absolute; left: 108px; width: 984px; height: 172px; border-radius: 4px;
    color: var(--white); font-size: 54px; display: flex; align-items: center;
  }
  .btn-login {
    top: 900px; background: var(--orange); justify-content: center; font-size: 58px;
  }
  .divider {
    position: absolute; left: 108px; width: 984px; top: 1196px; height: 18px;
    background: var(--divider); border-radius: 9px;
  }
  .divider__badge {
    position: absolute; left: 534px; top: 1137px; width: 132px; height: 136px;
    border-radius: 50%; background: var(--divider); color: var(--ink);
    display: flex; align-items: center; justify-content: center; font-size: 46px;
  }
  .btn-register { top: 1340px; background: var(--blue); padding-left: 197px; }
  .btn-social { top: 1560px; background: var(--navy); padding-left: 197px; }
  .btn-register__icon { position: absolute; left: 62px; top: 42px; }
  .groceries {
    position: absolute; left: 0; right: 0; bottom: 0; height: 470px;
    background:
      linear-gradient(180deg, rgba(166,150,196,1) 0%, rgba(166,150,196,0.55) 30%, rgba(140,120,175,0.35) 100%),
      linear-gradient(90deg, var(--wood) 0%, var(--leaf) 18%, var(--tomato) 34%, var(--cream) 52%, var(--pasta) 72%, var(--olive) 90%, var(--wood) 100%);
  }
</style>
</head>
<body>
  <div class="brand">basko</div>

  <div class="btn-wide btn-login">Login</div>

  <div class="divider"></div>
  <div class="divider__badge">OR</div>

  <div class="btn-wide btn-register">
    <svg class="btn-register__icon" width="88" height="88" viewBox="0 0 44 44" fill="none" stroke="#ffffff" stroke-width="2.6" stroke-linejoin="round">
      <path d="M6 5h24v8M30 27v12H6V5"/>
      <path d="M11 13h13M11 19h11M11 25h8M11 31h8" stroke-linecap="round"/>
      <path d="M36 10l5 5-15 15-7 2 2-7z"/>
    </svg>
    Register
  </div>
  <div class="btn-wide btn-social">Linkup login</div>

  <div class="groceries" role="img" aria-label="Photo of fresh groceries on a table: tomatoes, basil, olives, pasta, cheese and spices"></div>
</body>
</html>
```